BRIGHT PEAK POWER.

I'd like my business logo.
contact name: Daniel Fitzhume
phone:0407395182
email: info@brightpeakpower.net.au
website: www.brightpeakpower.net.au

services:
solar
battery storage
LED lighting
energy saving solutions
general electrical
I'd like the design to look professional

Target Market(s)

Everyone

Industry/Entity Type

Business

Contact Information for Business Card

as described above

Requirements
Must have
• Id like the colours and the design to work well with my logo.

```html
<!DOCTYPE html>
<html lang="en">
<head>
<meta charset="utf-8">
<title>Bright Peak Power – Business Card</title>
<link href="https://fonts.googleapis.com/css2?family=Open+Sans:wght@400;600;700&display=swap" rel="stylesheet">
<style>
  :root {
    --page: #e7e4df;
    --card: #050505;
    --green: #6cbf3f;
    --green-light: #a4d13a;
    --yellow: #ffc619;
    --orange: #f5821f;
    --text: #f2f2f2;
    --ghost: #1a1a1a;
  }
  * { margin: 0; padding: 0; box-sizing: border-box; }
  html, body { width: 1200px; height: 1000px; overflow: hidden; }
  body {
    background: var(--page);
    font-family: "Open Sans", Arial, sans-serif;
    position: relative;
  }
  .card {
    position: absolute;
    left: 150px; top: 232px;
    width: 900px; height: 536px;
    background: var(--card);
    border-radius: 27px;
    overflow: hidden;
    box-shadow: 0 10px 30px rgba(0,0,0,.25);
  }
  .brand {
    position: absolute;
    left: 42px; top: 78px;
    display: flex; align-items: center; gap: 16px;
  }
  .brand-dot {
    width: 54px; height: 54px; border-radius: 50%;
    background: var(--orange);
  }
  .brand-name {
    font-weight: 700; font-size: 40px; letter-spacing: 1px;
    color: var(--green);
  }
  .brand-ghost {
    position: absolute;
    left: 470px; top: 60px;
    width: 380px; height: 380px; border-radius: 50%;
    background: var(--ghost);
  }
  .person { position: absolute; left: 45px; top: 272px; }
  .person-name { font-weight: 700; font-size: 32px; color: var(--green); line-height: 1.15; }
  .person-title { font-size: 21px; color: var(--text); line-height: 1.3; }
  .contacts { position: absolute; left: 42px; top: 376px; list-style: none; }
  .contacts li {
    display: flex; align-items: center; gap: 8px;
    font-size: 21px; color: var(--text); height: 34px;
  }
  .contacts svg { width: 20px; height: 20px; fill: var(--orange); }
  .services { position: absolute; left: 558px; top: 252px; }
  .services h2 { font-weight: 700; font-size: 24px; color: var(--green); line-height: 32px; }
  .services ul { list-style: none; }
  .services li {
    display: flex; align-items: center; gap: 10px;
    font-size: 21px; color: var(--text); height: 33.7px;
  }
  .services svg { width: 18px; height: 18px; stroke: var(--orange); fill: none; stroke-width: 3; }
  .bands { position: absolute; left: 0; top: 0; }
</style>
</head>
<body>
  <div class="card">
    <div class="brand-ghost"></div>
    <div class="brand">
      <span class="brand-dot"></span>
      <span class="brand-name">BRIGHT PEAK POWER</span>
    </div>

    <div class="person">
      <div class="person-name">Daniel Fitzhume</div>
      <div class="person-title">President</div>
    </div>

    <ul class="contacts">
      <li><svg viewBox="0 0 24 24"><path d="M6.6 10.8a15 15 0 0 0 6.6 6.6l2.2-2.2c.3-.3.7-.4 1-.2 1.1.4 2.3.6 3.6.6.6 0 1 .4 1 1V20c0 .6-.4 1-1 1A17 17 0 0 1 3 4c0-.6.4-1 1-1h3.5c.6 0 1 .4 1 1 0 1.3.2 2.5.6 3.6.1.3 0 .7-.2 1z"/></svg>0407395182</li>
      <li><svg viewBox="0 0 24 24"><path d="M2 5h20v14H2z M2 5l10 8 10-8" /><path d="M3 6l9 7 9-7v-.5H3z" fill="#050505"/></svg>info@brightpeakpower.net.au</li>
      <li><svg viewBox="0 0 24 24"><circle cx="12" cy="12" r="10"/><path d="M2 12h20M12 2c3 3 3 17 0 20M12 2c-3 3-3 17 0 20" stroke="#050505" stroke-width="1.6" fill="none"/></svg>www.brightpeakpower.net.au</li>
    </ul>

    <section class="services">
      <h2>SERVICES</h2>
      <ul>
        <li><svg viewBox="0 0 20 20"><path d="M3 10l5 5 9-11"/></svg>Solar</li>
        <li><svg viewBox="0 0 20 20"><path d="M3 10l5 5 9-11"/></svg>Battery storage</li>
        <li><svg viewBox="0 0 20 20"><path d="M3 10l5 5 9-11"/></svg>LED lighting</li>
        <li><svg viewBox="0 0 20 20"><path d="M3 10l5 5 9-11"/></svg>Energy saving solutions</li>
        <li><svg viewBox="0 0 20 20"><path d="M3 10l5 5 9-11"/></svg>General electrical</li>
      </ul>
    </section>

    <svg class="bands" width="900" height="536" viewBox="0 0 900 536">
      <defs>
        <linearGradient id="band-green" x1="0" x2="1">
          <stop offset="0" stop-color="var(--green)"/>
          <stop offset="1" stop-color="var(--green-light)"/>
        </linearGradient>
        <linearGradient id="band-orange" x1="0" x2="1">
          <stop offset="0" stop-color="var(--yellow)"/>
          <stop offset="1" stop-color="var(--orange)"/>
        </linearGradient>
      </defs>
      <polygon points="0,512 479,512 455,536 0,536" fill="url(#band-green)"/>
      <polygon points="522,493 900,493 900,536 468,536" fill="url(#band-orange)"/>
    </svg>
  </div>
</body>
</html>
```